Out Door Living brochure

We need a Great looking brochure to feature the latest in out door living. Showcasing out doors is the new living space.

I'm enclosing our logo and a brochure we had done recently it didn't have enough impact. This one was a single fold you can also provide a tri fold if you see fit. We like the verbiage, but if you can spice it up we would love to see that. This brochure will be added to our sales packet.
Thank you!!!

Target Market(s)

Home owners

Industry/Entity Type

Construction Company

Logo Text

(See logo) Beautiful Homes Built to Last Introducing Outdoor living 2017

Font styles to use
Serif

Requirements
Must have
• Logo and
• Beautiful Homes Built to Last
• Introducing Outdoor living 2017
Nice to have
• Benefits of outdoor living
Should not have
• Bad photos if these don't work let me know we can get others to replace the sapce

```html
<!DOCTYPE html>
<html lang="en">
<head>
<meta charset="utf-8">
<title>Outdoor Living 2017 Brochure</title>
<link href="https://fonts.googleapis.com/css2?family=Quicksand:wght@500;600;700&family=Open+Sans:ital,wght@0,400;0,600;0,700;1,600&display=swap" rel="stylesheet">
<style>
  :root {
    --blue: #3aa4e6;
    --blue-light: #8fcdf3;
    --charcoal: #3c3c3e;
    --ink: #474749;
    --paper: #ffffff;
    --stage: #e6e7e9;
    --photo-sky: #8fc3e6;
    --photo-stone: #7d8890;
    --photo-warm: #b7865a;
    --photo-green: #6f8f5c;
  }
  * { box-sizing: border-box; margin: 0; padding: 0; }
  html, body { width: 1200px; height: 998px; overflow: hidden; }
  body { background: var(--stage); font-family: "Open Sans", sans-serif; color: var(--ink); }

  .spread {
    position: absolute; left: 60px; width: 1080px; height: 465px;
    display: flex; box-shadow: 0 6px 18px rgba(0,0,0,.18);
  }
  .spread--outside { top: 24px; }
  .spread--inside { top: 509px; }

  .page { position: relative; width: 540px; height: 465px; background: var(--paper); overflow: hidden; }
  .page + .page { border-left: 1px solid rgba(0,0,0,.08); }
  .page__art { position: absolute; inset: 0; width: 540px; height: 465px; }
  .page__text { position: absolute; }

  .heading { font-family: "Quicksand", sans-serif; }

  /* outside back */
  .back__tagline { top: 18px; right: 22px; width: 300px; text-align: right; color: #fff; font-size: 16px; font-weight: 600; line-height: 1.3; text-shadow: 0 1px 3px rgba(0,0,0,.4); }
  .back__staycation { top: 196px; right: 26px; width: 330px; text-align: right; font-size: 22px; font-weight: 600; line-height: 1.25; color: var(--ink); }
  .brand { display: flex; align-items: center; gap: 8px; font-family: "Open Sans", sans-serif; font-weight: 600; font-size: 12px; letter-spacing: .08em; text-transform: uppercase; }
  .brand__mark { width: 12px; height: 12px; border-radius: 50%; background: currentColor; flex: none; }
  .back__brand { top: 340px; left: 30px; color: #fff; }
  .contact { top: 364px; left: 30px; color: #fff; font-size: 11.5px; font-style: normal; line-height: 1.45; }
  .contact__phone { font-size: 14px; font-weight: 600; }

  /* outside front */
  .front__badge { top: 218px; left: 200px; width: 140px; text-align: center; color: var(--blue); font-size: 11px; }
  .front__badge .brand { flex-direction: column; gap: 0; line-height: 1.3; }
  .front__title { top: 318px; right: 30px; width: 420px; text-align: right; color: #fff; font-size: 36px; font-weight: 600; line-height: 1.1; }
  .front__url { top: 412px; right: 40px; width: 380px; padding: 4px 0; border-radius: 14px; background: #fff; text-align: center; color: var(--ink); font-size: 14px; letter-spacing: .06em; box-shadow: 0 2px 4px rgba(0,0,0,.25); }

  /* inside left */
  .evolved__title { top: 26px; left: 60px; width: 420px; padding: 5px 0; border: 2px solid var(--blue); border-radius: 18px; text-align: center; color: var(--blue); font-style: italic; font-weight: 600; font-size: 20px; }
  .evolved__body { top: 78px; left: 40px; width: 460px; text-align: center; font-size: 14px; line-height: 1.4; color: var(--ink); }

  /* inside right */
  .oasis__brand { top: 240px; left: 40px; width: 150px; color: var(--ink); font-size: 11px; line-height: 1.3; }
  .oasis__headline { top: 226px; right: 30px; width: 290px; font-size: 18px; font-weight: 700; line-height: 1.25; color: var(--ink); }
  .oasis__caption { top: 420px; left: 170px; color: #fff; font-size: 17px; font-weight: 700; font-family: "Quicksand", sans-serif; }
  .oasis__url { top: 442px; right: 26px; color: #fff; font-size: 11px; letter-spacing: .06em; }
</style>
</head>
<body>

<section class="spread spread--outside">
  <article class="page page--back">
    <svg class="page__art" viewBox="0 0 540 465">
      <defs>
        <linearGradient id="backPhoto" x1="0" y1="0" x2="1" y2="1">
          <stop offset="0" stop-color="var(--photo-stone)"/>
          <stop offset=".6" stop-color="#6fa9c4"/>
          <stop offset="1" stop-color="#c9d2d7"/>
        </linearGradient>
      </defs>
      <path role="img" aria-label="Photo of a modern deck with a stone planter, palm and glass rail" d="M0 0H540V165C400 195 200 245 0 272Z" fill="url(#backPhoto)"/>
      <path d="M0 272C200 245 400 195 540 165V180C400 210 200 258 0 286Z" fill="var(--blue)"/>
      <path d="M0 290C180 318 380 285 540 312V465H0Z" fill="var(--blue)"/>
      <path d="M0 306C180 334 380 300 540 328V465H0Z" fill="var(--charcoal)"/>
      <path d="M380 465L540 372V465Z" fill="var(--blue)"/>
    </svg>
    <p class="page__text back__tagline">Innovative ideas that help stretch out the seasons, making it comfy and cozy.</p>
    <p class="page__text back__staycation heading">Enjoy your staycation in the comfort of your own back yard</p>
    <div class="page__text brand back__brand"><span class="brand__mark"></span>Harbor Crest Builders</div>
    <address class="page__text contact">
      <span class="contact__phone">CALL: 555-014-2290</span><br>
      sam.ortiz@example.net<br>
      www.harborcrestbuilders.com<br>
      1480 Marina Vista Road, Bayview, CA 90000<br>
      HARBOR CREST
    </address>
  </article>

  <article class="page page--front">
    <svg class="page__art" viewBox="0 0 540 465">
      <defs>
        <linearGradient id="frontPhoto" x1="0" y1="0" x2="0" y2="1">
          <stop offset="0" stop-color="var(--photo-sky)"/>
          <stop offset=".55" stop-color="var(--photo-stone)"/>
          <stop offset="1" stop-color="var(--photo-green)"/>
        </linearGradient>
      </defs>
      <rect width="540" height="465" fill="var(--blue)"/>
      <path role="img" aria-label="Photo of a covered outdoor kitchen beside a lake with palm trees" d="M0 0H540V232C420 252 300 250 0 276Z" fill="url(#frontPhoto)"/>
      <path d="M0 276C300 250 420 252 540 232V246C420 266 300 264 0 290Z" fill="var(--charcoal)"/>
      <path d="M0 290C300 264 420 266 540 246V256C420 276 300 274 0 300Z" fill="var(--blue-light)"/>
      <circle cx="270" cy="252" r="62" fill="#fff" stroke="var(--blue)" stroke-width="6"/>
    </svg>
    <div class="page__text front__badge"><div class="brand">Harbor Crest<br>Builders</div></div>
    <h1 class="page__text front__title heading">Introducing<br>Outdoor living 2017</h1>
    <p class="page__text front__url">www.harborcrestbuilders.com</p>
  </article>
</section>

<section class="spread spread--inside">
  <article class="page page--evolved">
    <svg class="page__art" viewBox="0 0 540 465">
      <defs>
        <linearGradient id="poolPhoto" x1="0" y1="0" x2="0" y2="1">
          <stop offset="0" stop-color="var(--photo-sky)"/>
          <stop offset=".45" stop-color="#6aa7c0"/>
          <stop offset="1" stop-color="var(--photo-warm)"/>
        </linearGradient>
      </defs>
      <path d="M0 176C200 146 400 146 540 170V184C400 160 200 160 0 190Z" fill="var(--blue)"/>
      <path role="img" aria-label="Photo of a patio dining set under an umbrella beside a pool at sunset" d="M0 190C200 160 400 160 540 184V465H0Z" fill="url(#poolPhoto)"/>
      <path d="M360 465C450 430 515 385 540 330V465Z" fill="var(--blue)"/>
    </svg>
    <h2 class="page__text evolved__title">The outdoor experience has evolved.</h2>
    <p class="page__text evolved__body">It used to be a Emberline grill, tables and a few chairs. Now we have whole kitchens, outdoors fireplaces, and waterproof electronics to extend the season.</p>
  </article>

  <article class="page page--oasis">
    <svg class="page__art" viewBox="0 0 540 465">
      <defs>
        <linearGradient id="kitchenPhoto" x1="0" y1="0" x2="1" y2="0">
          <stop offset="0" stop-color="#6b6258"/>
          <stop offset=".6" stop-color="var(--photo-stone)"/>
          <stop offset="1" stop-color="var(--photo-sky)"/>
        </linearGradient>
        <linearGradient id="firePhoto" x1="0" y1="0" x2="1" y2="1">
          <stop offset="0" stop-color="#8a7a66"/>
          <stop offset=".5" stop-color="#5e5a56"/>
          <stop offset="1" stop-color="#a06a4e"/>
        </linearGradient>
      </defs>
      <path role="img" aria-label="Photo of an outdoor kitchen bar with stools under a timber roof" d="M0 0H540V60C470 150 330 200 0 205Z" fill="url(#kitchenPhoto)"/>
      <path d="M0 205C330 200 470 150 540 60V90C460 180 320 215 0 218Z" fill="var(--blue)"/>
      <path d="M0 218C320 215 460 180 540 90V110C450 195 320 228 0 226Z" fill="var(--blue-light)"/>
      <path d="M540 280C520 330 470 380 0 410V465H540Z" fill="var(--blue)"/>
      <path d="M540 380C500 420 420 440 260 465H540Z" fill="var(--charcoal)"/>
      <rect x="84" y="302" width="392" height="114" rx="12" fill="var(--charcoal)"/>
      <rect role="img" aria-label="Photo of a granite fire pit table with a glass wind guard" x="92" y="308" width="376" height="102" rx="8" fill="url(#firePhoto)"/>
    </svg>
    <div class="page__text brand oasis__brand"><span class="brand__mark" style="color:var(--blue)"></span><span>Harbor Crest<br>Builders</span></div>
    <h2 class="page__text oasis__headline">Transform your outdoor space into an oasis you may never want to leave.</h2>
    <p class="page__text oasis__caption">Fire pit arbor</p>
    <p class="page__text oasis__url">www.harborcrestbuilders.com</p>
  </article>
</section>

</body>
</html>
```